International Wine Label 202001

Need a wine label designed for several new wines from California being exported to Asia. This label should be focused around an animal theme of the flowing: Tiger, Lion, Horse or Eagle. The label should be adaptable to a product line of wines. For example the label could be used for a Cabernet wine, Merlot, Chardonnay or Pinot. A slight modification to the label design should be incorporated to allow for the different varietals. Front label design only. Can utilize photo image in design.
The label would be around 5.75" x 3.50".

Target Market(s)

25-35 year old wine buyers in the global market

Industry/Entity Type

Retail

Font styles to use
Sans Serif

Requirements
Must have
• Wine name based on design (designer suggest name)
Wine varietals
Vintage date
Additional wording area
Nice to have
• Rectangular label preferred Front label only.

```html
<!DOCTYPE html>
<html lang="en">
<head>
<meta charset="utf-8">
<title>Solmane Cabernet Sauvignon Label</title>
<link rel="stylesheet" href="https://fonts.googleapis.com/css2?family=Montserrat:wght@400;700&family=Oswald:wght@400&display=swap">
<style>
  :root {
    --backdrop: #e4e5e9;
    --label-white: #f1f1f1;
    --gold: #b68b24;
    --gold-light: #d8b655;
    --gold-text: #b3872a;
    --lion-tone: #f4f2ec;
  }
  * { margin: 0; padding: 0; box-sizing: border-box; }
  html, body {
    width: 1200px;
    height: 1200px;
    overflow: hidden;
    background: var(--backdrop);
  }
  .canvas {
    position: relative;
    width: 1200px;
    height: 1200px;
  }
  .label {
    position: absolute;
    left: 350px;
    top: 60px;
    width: 500px;
    height: 1080px;
    background: var(--label-white);
    overflow: hidden;
    box-shadow: 0 10px 30px rgba(0,0,0,0.08);
  }
  .label-art {
    position: absolute;
    left: 0;
    top: 0;
    width: 500px;
    height: 400px;
  }
  .brand-name {
    position: absolute;
    left: 36px;
    top: 505px;
    font-family: "Montserrat", sans-serif;
    font-weight: 700;
    font-size: 42px;
    letter-spacing: 2px;
    color: var(--gold-text);
  }
  .varietal {
    position: absolute;
    left: 36px;
    top: 775px;
    font-family: "Oswald", sans-serif;
    font-weight: 400;
    font-size: 46px;
    line-height: 1;
    color: var(--gold-text);
  }
  .region {
    position: absolute;
    left: 36px;
    top: 842px;
    font-family: "Montserrat", sans-serif;
    font-weight: 400;
    font-size: 30px;
    letter-spacing: 3px;
    color: var(--gold-text);
  }
  .vintage {
    position: absolute;
    left: 36px;
    top: 882px;
    font-family: "Montserrat", sans-serif;
    font-weight: 400;
    font-size: 28px;
    letter-spacing: 2px;
    color: var(--gold-text);
  }
  .base-rule {
    position: absolute;
    left: 24px;
    right: 24px;
    top: 1020px;
    height: 8px;
    background: var(--gold);
  }
</style>
</head>
<body>
  <main class="canvas">
    <section class="label">
      <svg class="label-art" viewBox="0 0 500 400" xmlns="http://www.w3.org/2000/svg">
        <defs>
          <linearGradient id="goldBand" x1="0" y1="0" x2="1" y2="0">
            <stop offset="0" stop-color="var(--gold)"/>
            <stop offset="0.5" stop-color="var(--gold-light)"/>
            <stop offset="1" stop-color="var(--gold)"/>
          </linearGradient>
        </defs>
        <path class="gold-band" fill="url(#goldBand)"
              d="M0 0 H500 V300 C440 300 380 290 320 310 C250 335 190 330 130 345 C80 357 40 370 0 372 Z"/>
        <rect class="lion-silhouette" role="img" aria-label="White silhouette of a standing lion in profile"
              x="60" y="60" width="310" height="250" rx="40" fill="var(--lion-tone)"/>
      </svg>
      <div class="brand-name">SOLMANE</div>
      <div class="varietal">Cabernet Sauvignon</div>
      <div class="region">NAPA VALLEY</div>
      <div class="vintage">2020</div>
      <div class="base-rule"></div>
    </section>
  </main>
</body>
</html>
```